Harlow Solutions Website

My business has been word of mouth over the last 3 years and has grown. Now I need a website for additional marketing as we have new clients asking for a website.

You have already completed my Logo during an earlier project. I have attached the logo.

We do Staff Augmentation and Operation Support.

What is that?
Staff augmentation is an outsourcing strategy that allows companies to fill specific, temporary roles to achieve business objectives. This staffing method complements existing teams with specific talent, enhancing business capabilities or filling gaps left by members on extended leave.

We work alongside the internal recruiting team to assist clients to meet and exceed financial goals.

```html
<!DOCTYPE html>
<html lang="en">
<head>
<meta charset="utf-8">
<title>Harlow Solutions</title>
<link href="https://fonts.googleapis.com/css2?family=Montserrat:wght@500;600;700&family=Roboto:ital,wght@0,400;0,500;1,400&display=swap" rel="stylesheet">
<style>
:root{
  --navy:#0f4f78;
  --navy-dark:#0a3a5c;
  --grey:#6f7073;
  --grey-band:#8a8b8d;
  --footer:#585455;
  --text:#2c2c2c;
  --muted:#8a8a8a;
  --white:#ffffff;
}
*{margin:0;padding:0;box-sizing:border-box}
html,body{width:1200px;height:4373px;overflow:hidden}
body{position:relative;background:var(--white);font-family:"Roboto",Arial,sans-serif;color:var(--text)}
.abs{position:absolute}
.lines{white-space:nowrap}

/* header */
.top-line{left:0;top:0;width:1200px;height:6px;background:var(--navy)}
.phone-tab{left:849px;top:0;width:263px;height:51px;background:var(--navy);border-radius:0 0 130px 130px/0 0 51px 51px;color:var(--white);font:600 17px "Montserrat",sans-serif;text-align:center;line-height:44px}
.brand{left:63px;top:26px;display:flex;align-items:center;gap:16px}
.brand-dot{width:70px;height:70px;border-radius:50%;background:var(--navy);flex:none}
.brand-name{font:600 27px "Montserrat",sans-serif;color:var(--navy);letter-spacing:1px;line-height:29px}
.main-nav{left:458px;top:83px;font:500 18px "Montserrat",sans-serif;color:var(--grey)}
.main-nav span{position:absolute;white-space:nowrap}
.main-nav .active{color:var(--navy)}

/* hero */
.hero{left:0;top:129px;width:1200px;height:669px;background:
  radial-gradient(circle at 29% 45%,rgba(190,220,250,.85) 0%,rgba(95,150,210,.7) 12%,rgba(30,80,150,0) 38%),
  radial-gradient(ellipse at 82% 32%,rgba(205,210,225,.75) 0%,rgba(120,135,165,.45) 18%,rgba(20,40,80,0) 40%),
  radial-gradient(ellipse at 75% 10%,rgba(60,70,95,.9) 0%,rgba(10,25,55,0) 35%),
  linear-gradient(100deg,#1d4f91 0%,#2a63a8 30%,#163a72 55%,#0d2550 80%,#0a1b3c 100%)}
.hero-curve{left:0;top:680px;width:1200px;height:120px}

/* welcome */
.welcome-mark{left:195px;top:875px;width:360px;height:360px;border-radius:50%;background:radial-gradient(circle at 40% 40%,#1a6494,#0f4f78 60%,#0a3a5c);display:flex;align-items:center;justify-content:center;text-align:center;color:var(--white);font:600 30px "Montserrat",sans-serif;line-height:38px;letter-spacing:1px}
.welcome-text{left:631px;top:940px;width:440px}
.title-grey{font:600 36px "Montserrat",sans-serif;color:var(--grey);line-height:42px}
.title-navy{font:700 36px "Montserrat",sans-serif;color:var(--navy);line-height:42px}
.body-copy{font-size:15px;line-height:22.5px;color:var(--text)}
.btn{display:inline-block;background:var(--navy);color:var(--white);font:700 16px "Montserrat",sans-serif;padding:0 22px;height:48px;line-height:48px}

/* services */
.service-left{left:0;top:1422px;width:600px;height:577px;background:
  radial-gradient(ellipse at 58% 28%,rgba(215,210,215,.55) 0%,rgba(150,170,195,0) 30%),
  radial-gradient(ellipse at 18% 62%,rgba(180,195,215,.5) 0%,rgba(120,150,180,0) 28%),
  linear-gradient(160deg,#7d9bb8 0%,#5a7fa3 35%,#3c6188 65%,#26425f 100%)}
.service-right{left:600px;top:1422px;width:600px;height:577px;background:
  radial-gradient(ellipse at 80% 55%,rgba(170,70,80,.55) 0%,rgba(140,60,70,0) 35%),
  radial-gradient(ellipse at 55% 15%,rgba(230,228,225,.8) 0%,rgba(200,198,195,0) 35%),
  linear-gradient(200deg,#b9b5af 0%,#a7a29c 40%,#8b8681 70%,#6e6a67 100%)}
.label-staff{left:243px;top:1738px;width:357px;height:64px;background:var(--navy);clip-path:polygon(40px 0,100% 0,100% 100%,0 100%);color:var(--white);font:600 19px "Montserrat",sans-serif;line-height:64px;padding-left:48px}
.label-ops{left:600px;top:1620px;width:379px;height:65px;background:var(--grey-band);clip-path:polygon(0 0,100% 0,calc(100% - 40px) 100%,0 100%);color:var(--white);font:600 19px "Montserrat",sans-serif;line-height:65px;padding-left:96px}
.service-hub{left:507px;top:1618px;width:186px;height:186px;border-radius:50%;background:var(--white)}

/* recruiting */
.section-title{left:0;width:1200px;text-align:center;font:600 36px "Montserrat",sans-serif;line-height:42px}
.sub-title{left:149px;top:2250px;width:420px;font:600 26px "Montserrat",sans-serif;color:var(--grey);line-height:32px}
.recruit-copy{left:151px;top:2342px;width:420px}
.recruit-photo{left:599px;top:2242px;width:451px;height:441px;background:
  radial-gradient(ellipse at 55% 25%,rgba(60,100,150,.7) 0%,rgba(60,100,150,0) 22%),
  radial-gradient(ellipse at 62% 62%,rgba(225,220,210,.85) 0%,rgba(200,190,170,0) 25%),
  radial-gradient(ellipse at 15% 75%,rgba(70,100,130,.6) 0%,rgba(70,100,130,0) 22%),
  linear-gradient(160deg,#2b2520 0%,#5a4432 30%,#8a6747 55%,#7a5a3e 80%,#4a3828 100%)}

/* testimonial */
.testimonial{left:0;top:2803px;width:1200px;height:472px;background:
  radial-gradient(ellipse at 12% 30%,rgba(90,140,200,.75) 0%,rgba(60,110,170,0) 30%),
  radial-gradient(ellipse at 35% 15%,rgba(120,150,190,.5) 0%,rgba(90,120,170,0) 22%),
  radial-gradient(ellipse at 75% 70%,rgba(70,110,170,.55) 0%,rgba(50,90,150,0) 30%),
  linear-gradient(110deg,#1e4a86 0%,#2c4f80 35%,#1a3560 65%,#0b1a36 100%)}
.quote-badge{left:554px;top:2880px;width:92px;height:92px;border-radius:50%;background:var(--white)}
.quote-text{left:150px;top:3012px;width:900px;text-align:center;font:italic 400 21px "Roboto",sans-serif;line-height:29.5px;color:var(--white)}
.quote-name{left:0;top:3160px;width:1200px;text-align:center;font:400 25px "Roboto",sans-serif;color:var(--white)}

/* news */
.news-card{top:3459px;width:280px}
.news-photo{width:280px;height:242px}
.news-title{margin-top:18px;font:600 21px "Montserrat",sans-serif;color:var(--navy);line-height:25px}
.news-text{margin-top:22px;font-size:14.5px;line-height:22.5px;color:var(--muted)}
.news-date{margin-top:26px;display:inline-block;background:var(--navy);color:var(--white);font-size:16px;width:120px;height:36px;line-height:36px;text-align:center}

/* footer */
.footer-bg{left:0;top:3960px;width:1200px;height:413px}
.footer-brand{left:0;top:4090px;width:1200px;display:flex;justify-content:center;align-items:center;gap:16px}
.footer-brand .brand-dot{background:var(--white);width:78px;height:78px}
.footer-brand .brand-name{color:var(--white);font-size:30px;line-height:32px}
.footer-nav{left:0;top:4240px;width:1200px;font:600 18px "Montserrat",sans-serif;color:var(--white)}
.footer-nav span{position:absolute;white-space:nowrap}
.copyright{left:0;top:4304px;width:1200px;text-align:center;font-size:16px;color:var(--white)}
</style>
</head>
<body>

<header>
  <div class="abs top-line"></div>
  <div class="abs phone-tab">PH:555 010 4471</div>
  <div class="abs brand">
    <span class="brand-dot"></span>
    <span class="brand-name">HARLOW<br>SOLUTIONS, LLC</span>
  </div>
  <nav class="abs main-nav">
    <span class="active" style="left:0">HOME</span>
    <span style="left:114px">ABOUT</span>
    <span style="left:241px">WHAT WE DO</span>
    <span style="left:426px">CLIENTS</span>
    <span style="left:559px">CONTACT</span>
  </nav>
</header>

<section>
  <div class="abs hero" role="img" aria-label="Hand touching a glowing digital outsourcing interface ringed with business icons"></div>
  <svg class="abs hero-curve" viewBox="0 0 1200 120" preserveAspectRatio="none">
    <path d="M0 24 Q600 90 1200 12 L1200 120 L0 120 Z" fill="#ffffff"/>
    <path d="M105 42 Q600 150 1110 42 Q600 100 105 42 Z" fill="#0f4f78"/>
  </svg>
</section>

<section>
  <div class="abs welcome-mark">HARLOW<br>SOLUTIONS</div>
  <div class="abs welcome-text">
    <h1 class="title-grey">WELCOME TO</h1>
    <h2 class="title-navy">HARLOW SOLUTIONS</h2>
    <p class="body-copy lines" style="margin-top:20px">Lorem ipsum dolor sit amet, consectetur adipiscing elit,<br>sed do eiusmod tempor incididunt ut labore et dolore<br>magna aliqua. Quis ipsum suspendisse ultrices gravida.<br>Risus commodo viverra maecenas accumsan lacus vel<br>facilisis. Lorem ipsum dolor sit amet, consectetur adipis<br>cing elit, sed do eiusmod tempor incididunt ut labore et<br>dolore magna aliqua. Quis ipsum suspendisse ultrices<br>gravidaus commodo viverra maecenas</p>
    <a class="btn" style="margin-top:18px">READ MORE</a>
  </div>
</section>

<section>
  <div class="abs service-left" role="img" aria-label="Smiling businesswoman shaking hands in a bright office meeting"></div>
  <div class="abs service-right" role="img" aria-label="Smiling support agent with headset working at a computer"></div>
  <div class="abs label-staff">STAFF AUGMENTATION</div>
  <div class="abs label-ops">OPERATION SUPPORT</div>
  <div class="abs service-hub" aria-hidden="true"></div>
</section>

<section>
  <h2 class="abs section-title" style="top:2092px;color:var(--grey)">WE WORK ALONGSIDE THE</h2>
  <h2 class="abs section-title" style="top:2134px;color:var(--navy);font-weight:700">INTERNAL RECRUITING TEAM</h2>
  <h3 class="abs sub-title">To assist clients to meet and<br>exceed financial goals.</h3>
  <div class="abs recruit-copy">
    <p class="body-copy lines">Lorem ipsum dolor sit amet, consectetur adipiscing elit,<br>sed do eiusmod tempor incididunt ut labore et dolore<br>magna aliqua. Quis ipsum suspendisse ultrices gravida.<br>Risus commodo viverra maecenas accumsan lacus vel<br>facilisis. Lorem ipsum dolor sit amet, consectetur adipis<br>cing elit, sed do eiusmod tempor incididunt ut labore et<br>dolore magna aliqua. Quis ipsum suspendisse ultrices<br>gravidaus commodo viver. Lorem ipsum dolor sit amet,<br>consectetur adipis cing elit, sed do eiusmod tempor<br>incididunt ut labore et dolore magna aliqua. Quis ipsum<br>suspendisse ultrices gravidaus commodo viverra<br>maecenas</p>
    <a class="btn" style="margin-top:22px">READ MORE</a>
  </div>
  <div class="abs recruit-photo" role="img" aria-label="Team working together around a wooden table with laptop and notes"></div>
</section>

<section>
  <div class="abs testimonial" role="img" aria-label="Blurred blue office background"></div>
  <div class="abs quote-badge">
    <svg width="92" height="92" viewBox="0 0 92 92"><g fill="#0f4f78"><path d="M26 58 V46 Q26 32 38 30 V36 Q32 38 32 44 H40 V58 Z"/><path d="M50 58 V46 Q50 32 62 30 V36 Q56 38 56 44 H64 V58 Z"/></g></svg>
  </div>
  <p class="abs quote-text lines">“Lorem ipsum dolor sit amet, consectetur adipiscing eli ed do eiusmod<br>incididunt ut labore et dolore magna aliquauis ipsum suspendisse ultrices<br>gravidasus commodo viverra maecenas accumsan lacus vel facilisisorem<br>ipsum dolor sit amet, consectetur adipis cing d do eiusmo”</p>
  <p class="abs quote-name">Dana Whitfield</p>
</section>

<section>
  <h2 class="abs section-title" style="top:3360px;color:var(--grey)">LATEST <span style="color:var(--navy);font-weight:700">NEWS</span></h2>
  <article class="abs news-card" style="left:149px">
    <div class="news-photo" role="img" aria-label="Two colleagues reviewing a tablet" style="background:radial-gradient(ellipse at 30% 55%,rgba(210,180,150,.55) 0%,rgba(0,0,0,0) 30%),linear-gradient(160deg,#3a3f47,#6d7580 45%,#2a2e35)"></div>
    <h3 class="news-title">Lorelorm ipsum dolor<br>sit amet, consecte</h3>
    <p class="news-text lines">Lorem ipsum dolor sit amet, conse<br>ctetur adipiscing elit, sed do eius<br>mod tempor incididunt u</p>
    <span class="news-date">10-01-2022</span>
  </article>
  <article class="abs news-card" style="left:460px">
    <div class="news-photo" role="img" aria-label="Business handshake over a glowing digital globe" style="background:radial-gradient(ellipse at 75% 40%,rgba(170,225,240,.8) 0%,rgba(0,0,0,0) 30%),linear-gradient(160deg,#16243c,#2f5677 55%,#6f9fb8)"></div>
    <h3 class="news-title">Lorelorm ipsum dolor<br>sit amet, consecte</h3>
    <p class="news-text lines">Lorem ipsum dolor sit amet, conse<br>ctetur adipiscing elit, sed do eius<br>mod tempor incididunt u</p>
    <span class="news-date">10-01-2022</span>
  </article>
  <article class="abs news-card" style="left:769px">
    <div class="news-photo" role="img" aria-label="Smiling businesswoman shaking hands at a desk" style="background:radial-gradient(ellipse at 55% 60%,rgba(175,110,70,.7) 0%,rgba(0,0,0,0) 30%),linear-gradient(160deg,#e2e0dd,#c0b9b2 45%,#5a4a40)"></div>
    <h3 class="news-title">Lorelorm ipsum dolor<br>sit amet, consecte</h3>
    <p class="news-text lines">Lorem ipsum dolor sit amet, conse<br>ctetur adipiscing elit, sed do eius<br>mod tempor incididunt u</p>
    <span class="news-date">10-01-2022</span>
  </article>
</section>

<footer>
  <svg class="abs footer-bg" viewBox="0 0 1200 413" preserveAspectRatio="none">
    <path d="M0 20 Q600 80 1200 20 L1200 413 L0 413 Z" fill="#585455"/>
    <path d="M0 20 Q600 80 1200 20" fill="none" stroke="#0f4f78" stroke-width="6"/>
  </svg>
  <div class="abs footer-brand">
    <span class="brand-dot"></span>
    <span class="brand-name">HARLOW<br>SOLUTIONS, LLC</span>
  </div>
  <nav class="abs footer-nav">
    <span style="left:274px">HOME</span>
    <span style="left:387px">ABOUT</span>
    <span style="left:515px">WHAT WE DO</span>
    <span style="left:700px">CLIENTS</span>
    <span style="left:833px">CONTACT</span>
  </nav>
  <p class="abs copyright">© 2022 All Rights Reserved. Privacy Policy &nbsp;|&nbsp; Sitemap</p>
</footer>

</body>
</html>
```